Larvik Consulting

Hi,
I have my own network consulting business (just me)
and need to get a logo and business card design together,

Based in New Zealand,

Tobias Wrenfield
Unified Communications and Network Architect

/design engineer,
and would like this to be the basis for personal branding and company identity

Industry/Entity Type

Business

Requirements
Nice to have
• I have the basis for a optional logo - needs color -

```html
<!DOCTYPE html>
<html lang="en">
<head>
<meta charset="utf-8">
<title>Larvik Consulting – Business Cards</title>
<link href="https://fonts.googleapis.com/css2?family=Questrial&family=Arimo:wght@400;700&display=swap" rel="stylesheet">
<style>
  :root {
    --backdrop: #0a8ccc;
    --card-dark: #06202b;
    --card-dark-edge: #021118;
    --accent-cyan: #1fd8e8;
    --card-light: #ffffff;
    --card-light-border: #eeeeee;
    --navy: #113a63;
    --ink: #111111;
    --wordmark-light: #e9eef0;
  }
  * { margin: 0; padding: 0; box-sizing: border-box; }
  html, body { width: 1200px; height: 1200px; overflow: hidden; }
  body {
    background: var(--backdrop);
    position: relative;
    font-family: "Arimo", Arial, sans-serif;
  }
  .card {
    position: absolute;
    width: 690px;
    height: 394px;
  }
  .card--front {
    left: 80px;
    top: 180px;
    background: radial-gradient(ellipse at 55% 50%, #0b2e3b 0%, var(--card-dark) 55%, var(--card-dark-edge) 100%);
    display: flex;
    align-items: center;
    padding-left: 72px;
    gap: 36px;
  }
  .brand-dot {
    width: 150px;
    height: 150px;
    border-radius: 50%;
    background: var(--accent-cyan);
    flex: none;
  }
  .brand-name {
    font-family: "Questrial", "Century Gothic", sans-serif;
    font-size: 44px;
    color: var(--wordmark-light);
    white-space: nowrap;
  }
  .card--back {
    left: 440px;
    top: 640px;
    background: var(--card-light);
    border: 24px solid var(--card-light-border);
    display: flex;
    align-items: center;
    justify-content: space-between;
    padding: 0 36px 0 54px;
  }
  .contact {
    display: flex;
    align-items: stretch;
    gap: 12px;
  }
  .contact__icons {
    display: flex;
    flex-direction: column;
    justify-content: space-between;
    padding: 4px 10px 4px 0;
    border-right: 1.5px solid var(--navy);
  }
  .contact__icons svg { width: 26px; height: 26px; fill: var(--navy); display: block; }
  .contact__name { font-weight: 700; font-size: 23px; color: var(--ink); margin-bottom: 8px; }
  .contact__role, .contact__place { font-size: 15px; color: var(--ink); line-height: 1.3; }
  .contact__place { margin-top: 10px; }
  .logo-lockup {
    display: flex;
    align-items: center;
    gap: 14px;
  }
  .logo-lockup .brand-dot {
    width: 82px;
    height: 82px;
    background: var(--navy);
  }
  .logo-lockup .brand-name {
    font-size: 20px;
    color: var(--navy);
  }
</style>
</head>
<body>
  <section class="card card--front" aria-label="Business card front">
    <div class="brand-dot"></div>
    <span class="brand-name">Larvik Consulting</span>
  </section>

  <section class="card card--back" aria-label="Business card back">
    <div class="contact">
      <div class="contact__icons">
        <svg viewBox="0 0 24 24" aria-hidden="true"><circle cx="12" cy="7" r="5"/><path d="M2 23c0-6 4.5-9 10-9s10 3 10 9z"/></svg>
        <svg viewBox="0 0 24 24" aria-hidden="true"><path d="M3 1h18v22H3zM5 3v18h14V3z"/><rect x="7" y="5" width="5" height="5"/><rect x="13" y="5" width="4" height="1.6"/><rect x="13" y="8" width="4" height="1.6"/><rect x="7" y="12" width="10" height="1.6"/><rect x="7" y="15" width="10" height="1.6"/><rect x="7" y="18" width="10" height="1.6"/></svg>
        <svg viewBox="0 0 24 24" aria-hidden="true"><path d="M12 2 1 12h3v10h6v-6h4v6h6V12h3z"/></svg>
      </div>
      <div class="contact__text">
        <p class="contact__name">Tobias Wrenfield</p>
        <p class="contact__role">Unified Communications<br>and Network Architect</p>
        <p class="contact__place">New Zealand</p>
      </div>
    </div>
    <div class="logo-lockup">
      <div class="brand-dot"></div>
      <span class="brand-name">Larvik Consulting</span>
    </div>
  </section>
</body>
</html>
```